Business Card for an IT professional services company
Lakeshore Datavault Inc.
Business Card for an IT professional services company - Information Technology
Creative Brief
Professional
Martin Keswell
President
2718 5th Avenue SE Calgary, Alberta T2H 4B7
mart@lakeshoredatavault.example
www.lakeshoredatavault.example

```html
<!DOCTYPE html>
<html lang="en">
<head>
<meta charset="utf-8">
<title>Lakeshore Datavault Inc. — Business Card</title>
<link href="https://fonts.googleapis.com/css2?family=Roboto:wght@400;500;700&family=Roboto+Condensed:wght@400;700&display=swap" rel="stylesheet">
<style>
  :root{
    --bg-top:#e4e4e4;
    --bg-bottom:#cfcfcf;
    --card:#ffffff;
    --brand-blue:#1f5ea8;
    --accent-red:#c41e3a;
    --ink:#2e2e2e;
    --muted:#6b6b6b;
    --rule:#3a3a3a;
    --social-a:#c8203a;
    --social-b:#d6336c;
  }
  *{box-sizing:border-box;margin:0;padding:0}
  html,body{width:1200px;height:946px;overflow:hidden}
  body{
    background:linear-gradient(180deg,var(--bg-top),var(--bg-bottom));
    font-family:"Roboto",Arial,sans-serif;
    color:var(--ink);
    position:relative;
  }
  .card{
    position:absolute;
    left:320px;
    width:560px;height:320px;
    background:var(--card);
    border-radius:22px;
    box-shadow:0 14px 30px rgba(0,0,0,.18);
  }
  .card--back{top:80px}
  .card--front{top:486px}

  .brand{display:flex;align-items:center;gap:10px}
  .brand__mark{width:18px;height:18px;background:var(--brand-blue)}
  .brand__name{font-family:"Roboto",Arial,sans-serif;font-weight:500;color:var(--brand-blue);font-size:22px;letter-spacing:.2px}

  .card--back .brand{position:absolute;left:50%;top:118px;transform:translateX(-50%)}

  .social{position:absolute;right:34px;bottom:30px;display:flex;gap:18px;align-items:center}
  .social__item{display:flex;align-items:center;gap:6px;font-size:10px;color:var(--muted)}
  .social__sq{width:14px;height:14px;background:var(--social-a)}
  .social__item:nth-child(2) .social__sq{background:var(--social-b)}

  .card--front .brand{position:absolute;left:40px;top:48px}
  .contact{position:absolute;left:40px;top:104px;display:grid;grid-template-columns:30px 3px 1fr;column-gap:14px;row-gap:20px;align-items:center}
  .contact__icon{width:30px;height:30px;fill:var(--brand-blue)}
  .contact__rule{width:3px;height:100%;min-height:34px;background:var(--rule)}
  .contact__text{font-size:13px;line-height:1.45;color:var(--ink)}
  .person__name{font-family:"Roboto Condensed",Arial,sans-serif;font-weight:700;font-size:26px;letter-spacing:1px;color:var(--ink);line-height:1}
  .person__first{color:var(--accent-red)}
  .person__title{font-size:13px;color:var(--muted);margin-top:4px}
</style>
</head>
<body>
  <section class="card card--back" aria-label="Card back">
    <div class="brand">
      <span class="brand__mark"></span>
      <span class="brand__name">Lakeshore Datavault</span>
    </div>
    <div class="social">
      <span class="social__item"><span class="social__sq"></span>/lakeshore</span>
      <span class="social__item"><span class="social__sq"></span>/datavault</span>
    </div>
  </section>

  <section class="card card--front" aria-label="Card front">
    <div class="brand">
      <span class="brand__mark"></span>
      <span class="brand__name">Lakeshore Datavault</span>
    </div>
    <div class="contact">
      <svg class="contact__icon" viewBox="0 0 24 24" aria-hidden="true"><circle cx="12" cy="7" r="5"/><path d="M2 23c0-6 4.5-9 10-9s10 3 10 9z"/></svg>
      <span class="contact__rule"></span>
      <div class="contact__text person">
        <div class="person__name"><span class="person__first">MARTIN</span> KESWELL</div>
        <div class="person__title">President</div>
      </div>

      <svg class="contact__icon" viewBox="0 0 24 24" aria-hidden="true"><path d="M12 1a8 8 0 0 0-8 8c0 6 8 14 8 14s8-8 8-14a8 8 0 0 0-8-8zm0 11a3 3 0 1 1 0-6 3 3 0 0 1 0 6z"/></svg>
      <span class="contact__rule"></span>
      <div class="contact__text">
        2718 5th Avenue SE<br>Calgary, Alberta T2H 4B7
      </div>

      <svg class="contact__icon" viewBox="0 0 24 24" aria-hidden="true"><path d="M12 1a11 11 0 1 0 0 22 11 11 0 0 0 0-22zm7.9 10h-3.4a17 17 0 0 0-1.5-7 9 9 0 0 1 4.9 7zM12 3.1c1.2 1.6 2.3 4.4 2.5 7.9h-5c.2-3.5 1.3-6.3 2.5-7.9zM9 4a17 17 0 0 0-1.5 7H4.1A9 9 0 0 1 9 4zm-4.9 9h3.4a17 17 0 0 0 1.5 7 9 9 0 0 1-4.9-7zm7.9 7.9c-1.2-1.6-2.3-4.4-2.5-7.9h5c-.2 3.5-1.3 6.3-2.5 7.9zm3-.9a17 17 0 0 0 1.5-7h3.4a9 9 0 0 1-4.9 7z"/></svg>
      <span class="contact__rule"></span>
      <div class="contact__text">
        083 555 0142 &nbsp;|&nbsp; 012 555 0198<br>
        mart@lakeshoredatavault.example<br>
        www.lakeshoredatavault.example
      </div>
    </div>
  </section>
</body>
</html>
```